Leadership and Team Coaching Blog Template for my company, Fenwick Marlow Pty Ltd

I need a consistent design I can use for publications. I am a leadership coach as well as a team coach and I also am a pretty good facilitator. I am to help people be their best both as individuals and as teams so as I enter semi-retirement I've been writing short articles to support my business. The final design should be flexible and elegant so you can tell the difference between different articles. It should also communicate confidence, energy and expertise and invite you to read further. I love blue and have attached my current logo. Not wedded to using it but clients recognise it and am sure someone clever can do something interesting with it

Target Market(s)

middle and senior leaders and Board members

Industry/Entity Type

It Company

Font styles to use
Sans Serif

Colors
0392cd
3176b5
3276b5
886aae
33b8a4
00a990
a54499
c588bc
876aae

Requirements
Must have
• flexibility to be able to re-use for different publications
Nice to have
• eye catching images
• elegant line drawing
Should not have
• clip art

```html
<!DOCTYPE html>
<html lang="en">
<head>
<meta charset="utf-8">
<title>Fenwick Marlow — A Blog About People &amp; Change</title>
<link href="https://fonts.googleapis.com/css2?family=Gelasio:ital,wght@0,400;0,700;1,400;1,700&family=Open+Sans:wght@400;600&family=Oswald:wght@400;500&display=swap" rel="stylesheet">
<style>
:root{
  --navy:#0c2a5c;
  --topbar:#0a2350;
  --page:#f4f4f4;
  --title-blue:#2b6aa6;
  --ink:#2c2c2c;
  --button:#38b6ee;
  --footer:#2f2f2f;
  --white:#ffffff;
}
*{box-sizing:border-box;margin:0;padding:0}
html,body{width:1200px;height:3629px;overflow:hidden}
body{position:relative;background:var(--page);font-family:"Open Sans",Arial,sans-serif;color:var(--ink)}
.topbar{position:absolute;left:0;top:0;width:1200px;height:29px;background:var(--topbar)}
.topbar a{position:absolute;left:85px;top:6px;font:600 12px "Open Sans",sans-serif;color:var(--white);text-decoration:none}
.hero{position:absolute;left:0;top:29px;width:1200px;height:581px;
  background:linear-gradient(180deg,#5f7fa6 0%,#7f9cbf 30%,#45668e 60%,#1c3352 82%,#0d1a2c 100%)}
.hero-glow{position:absolute;left:420px;top:380px;width:360px;height:200px;border-radius:50%;
  background:radial-gradient(ellipse at center,rgba(255,214,160,.75),rgba(255,214,160,0) 70%)}
.brand{position:absolute;left:128px;top:96px;display:flex;align-items:center;gap:12px}
.brand-mark{width:26px;height:26px;background:var(--white)}
.brand-name{font:600 20px/1 "Open Sans",Arial,sans-serif;color:var(--white)}
.hero-band{position:absolute;left:285px;top:247px;width:670px;height:140px;background:rgba(90,90,90,.6)}
.hero-title{position:absolute;left:0;top:265px;width:1200px;text-align:center;
  font:400 64px/1 "Gelasio",Georgia,serif;letter-spacing:4px;color:var(--white)}
.hero-sub{position:absolute;left:0;top:340px;width:1200px;text-align:center;
  font:400 20px/1 "Oswald",sans-serif;letter-spacing:5px;color:#d8dde4}
.post{position:absolute;left:177px;width:561px}
.post-title{font:400 52px/62px "Gelasio",Georgia,serif;color:var(--title-blue)}
.post-date{margin-top:6px;font:italic 700 13px/1 "Gelasio",Georgia,serif;color:#222}
.post-text{margin-top:18px;font-size:12.6px;line-height:20px}
.post-photo{margin-top:18px;width:556px;height:368px;border:5px solid var(--white);
  box-shadow:0 10px 10px -6px rgba(0,0,0,.45);
  background:linear-gradient(135deg,#b79a8e 0%,#d9c5bd 30%,#5c6c86 55%,#1f3768 70%,#3e5878 100%)}
.read-more{display:block;margin-top:24px;width:125px;height:39px;background:var(--button);
  color:var(--white);font:600 12px/39px "Open Sans",sans-serif;text-align:center;text-decoration:none}
.signup{position:absolute;left:806px;top:665px;width:246px;height:296px;background:var(--navy);text-align:center;color:var(--white)}
.signup h2{margin-top:40px;font:400 50px/1 "Gelasio",Georgia,serif}
.signup p{margin-top:12px;font:500 15px/1 "Oswald",sans-serif;letter-spacing:1.5px}
.signup .field{position:absolute;left:26px;top:182px;width:192px;height:29px;background:var(--white);
  font:400 11px/29px "Gelasio",serif;color:#333;text-align:left;padding-left:8px}
.signup .submit{position:absolute;left:26px;top:221px;width:192px;height:34px;background:var(--button);
  font:400 12px/34px "Gelasio",serif;color:var(--white)}
.profile{position:absolute;left:806px;top:1028px;width:246px;height:673px;background:var(--white)}
.profile-photo{height:279px;background:linear-gradient(180deg,#e4e6e8 0%,#cfd6dd 55%,#7d9bbd 100%)}
.profile-name{margin:32px 0 0 20px;font:400 14px/1 "Oswald",sans-serif;letter-spacing:1.5px;color:#333}
.profile-role{margin:8px 0 0 20px;font:italic 400 11px/1 "Gelasio",serif;color:#444}
.profile-bio{margin:22px 20px 0;font:400 11.5px/17px "Gelasio",serif;color:#444;text-align:justify}
.profile-next{position:absolute;left:0;bottom:0;width:34px;height:32px;background:var(--button)}
.recent-head{position:absolute;left:806px;top:1759px;width:246px;height:44px;background:var(--navy);
  font:500 15px/44px "Oswald",sans-serif;letter-spacing:2px;color:var(--white);padding-left:18px}
.recent{position:absolute;left:820px;width:200px}
.recent a{display:block;font:400 16px/18px "Gelasio",Georgia,serif;color:#1f3b66;text-decoration:none}
.recent span{display:inline-block;margin-top:3px;font:400 11px/1 "Gelasio",serif;color:#444;text-decoration:underline}
.footer{position:absolute;left:0;top:3562px;width:1200px;height:67px;background:var(--footer)}
.social{position:absolute;top:27px;width:13px;height:13px;border-radius:50%;background:#8a8a8a}
.copyright{position:absolute;left:307px;top:26px;font:400 12px/1 "Open Sans",sans-serif;color:#9a9a9a}
.to-top{position:absolute;left:998px;top:24px}
</style>
</head>
<body>
<nav class="topbar"><a href="#">HOME</a></nav>

<header class="hero" role="img" aria-label="City skyline of tall towers under a cloudy blue sky with sun glowing on the horizon">
  <div class="hero-glow"></div>
</header>
<div class="brand"><span class="brand-mark"></span><span class="brand-name">Fenwick Marlow</span></div>
<div class="hero-band"></div>
<h1 class="hero-title">FENWICK MARLOW</h1>
<div class="hero-sub">A BLOG ABOUT PEOPLE &amp; CHANGE</div>

<article class="post" style="top:698px">
  <h2 class="post-title">A CEO's Guide to Strategic Growth</h2>
  <div class="post-date">March 30, 2016</div>
  <p class="post-text">To create a blog post, click here to open the Blog Manager. Edit your Published Post entitled 'A CEO's Guide to Strategic Growth', add your own text, images or videos, and click 'Publish'! From the Blog Manager you can also add a brand new post in a breeze.<br>Great looking images make your blog posts more visually compelling for your audience, so choose images that really wow.</p>
  <a class="read-more" href="#">Read More</a>
</article>

<article class="post" style="top:1102px">
  <h2 class="post-title">Business Tip: How to Poll Clients</h2>
  <div class="post-date">March 30, 2016</div>
  <div class="post-photo" role="img" aria-label="Speaker in a blue suit addressing a seated audience in a bright hall"></div>
  <p class="post-text">To create a blog post, click here to open the Blog Manager. Edit your Published Post entitled 'Business Tip: How to Poll Clients', add your own text, images or videos, and click 'Publish'! From the Blog Manager you can also add a brand new post in a breeze.<br>Adding fun and compelling videos is a great way to engage your audience and keep them coming back for more. Also, don't forget to use relevant keywords in your text for SEO purposes.</p>
  <a class="read-more" href="#">Read More</a>
</article>

<article class="post" style="top:1896px">
  <h2 class="post-title">10 Essentials for the Traveling Businessman</h2>
  <div class="post-date">March 30, 2016</div>
  <p class="post-text">To create a blog post, click here to open the Blog Manager. Edit your Published Post entitled '10 Essentials for the Traveling Businessman', add your own text, images or videos, and click 'Publish'! From the Blog Manager you can also add a brand new post in a breeze.<br>To make it easy for visitors to search your blog according to topic, add 'Tags' to your posts in the Blog Manager. You can showcase the very best posts from your blog by setting a post as a Featured Post. Just click the star icon next to the Post title to define it as a Featured Post. It's a great, easy way to promote specific content in your blog.</p>
  <a class="read-more" href="#">Read More</a>
</article>

<article class="post" style="top:2339px">
  <h2 class="post-title">Review of the Halden Report</h2>
  <div class="post-date">March 30, 2016</div>
  <div class="post-photo" role="img" aria-label="Speaker in a blue suit addressing a seated audience in a bright hall"></div>
  <p class="post-text">To create a blog post, click here to open the Blog Manager. Edit your Published Post entitled 'Review of the Halden Report', add your own text, images or videos, and click 'Publish'! From the Blog Manager you can also add a brand new post in a breeze.<br>To make it easy for visitors to search your blog according to topic, add 'Tags' to your posts in the Blog Manager. You can showcase the very best posts from your blog by setting a post as a Featured Post. Just click the star icon next to the Post title to define it as a Featured Post. It's a great, easy way to promote specific content in your blog.</p>
  <a class="read-more" href="#">Read More</a>
</article>

<article class="post" style="top:3190px">
  <h2 class="post-title">Profile: Tech Investor Ravi Tennant</h2>
  <div class="post-date">March 29, 2016</div>
  <p class="post-text">To create a blog post, click here to open the Blog Manager. Edit your Published Post entitled 'Profile: Tech Investor Ravi Tennant', add your own text, images or videos, and click 'Publish'! From the Blog Manager you can also add a brand new post in a breeze.<br>Adding fun and compelling videos is a great way to engage your audience and keep them coming back for more. Also, don't forget to use relevant keywords in your text for SEO purposes.</p>
  <a class="read-more" href="#">Read More</a>
</article>

<aside class="signup">
  <h2>Sign Up</h2>
  <p>AND STAY UPDATED!</p>
  <div class="field">Email Address</div>
  <div class="submit">Subscribe Now</div>
</aside>

<aside class="profile">
  <div class="profile-photo" role="img" aria-label="Portrait photo of a smiling man with glasses in a blue shirt"></div>
  <div class="profile-name">Mr. DANIEL HALE</div>
  <div class="profile-role">Director of Brightline Advisory</div>
  <p class="profile-bio">Lorem Ipsum is simply dummy text of the printing and typesetting industry. Lorem Ipsum has been the industry's standard dummy text ever since the 1500s, when an unknown printer took a galley of type and scrambled it to make a type specimen book.<br>It has survived not only five centuries, but also the leap into electronic typesetting, remaining essentially unchanged.</p>
  <div class="profile-next"><svg width="34" height="32" viewBox="0 0 34 32"><path d="M15 13l3 3-3 3" fill="none" stroke="#fff" stroke-width="1.5"/></svg></div>
</aside>

<div class="recent-head">RECENT POSTS</div>
<div class="recent" style="top:1820px"><a href="#">A CEO's Guide to Strategic Growth</a><span>March 30, 2016</span></div>
<div class="recent" style="top:1890px"><a href="#">Business Tip: How to Poll Clients</a><span>March 30, 2016</span></div>
<div class="recent" style="top:1958px"><a href="#">10 Essentials for the Traveling Businessman</a><span>March 30, 2016</span></div>
<div class="recent" style="top:2026px"><a href="#">Review of the Halden Report</a><span>March 30, 2016</span></div>
<div class="recent" style="top:2094px"><a href="#">Profile: Tech Investor Ravi Tennant</a><span>March 29, 2016</span></div>

<footer class="footer">
  <span class="social" style="left:177px"></span>
  <span class="social" style="left:208px"></span>
  <span class="social" style="left:239px"></span>
  <span class="social" style="left:270px"></span>
  <span class="copyright">© 2015 by Fenwick Marlow.</span>
  <svg class="to-top" width="22" height="16" viewBox="0 0 22 16"><path d="M3 13l8-8 8 8" fill="none" stroke="#8a8a8a" stroke-width="3"/></svg>
</footer>
</body>
</html>
```